earthmoving and roadworks company looking for a fresh and updated logo to help us stand out

We are looking for a business card design for our earthmoving, demolition and road works company named Wombridge Hire. We cover a broad range of work so our business card needs to be flexible to suit all of the different services we provide. We have a few different bits of machinery including several water trucks for transporting water and spraying the roads, an excavator (digger) for earthmoving, a tipper truck that carries grain/soil and other items, a skidmule and two rollers. our business card needs to be simple but effective and bold. Our colour palette is yellow, black and white and I have attached a copy of our logo but please note our logo is only the 'Wombridge hire' bit with attached circle, the 'watercarts, rollers, cartage' below are not part of the logo. Please feel free to modify the logo to better suit the business card. The design must be easy to read and to the point. It should make us look reliable and professional.

Target Market(s)

Wide range of clients including government sectors and private individuals

Industry/Entity Type

Construction

Contact Information for Business Card

We need a business card that is bold and straight to the point but with easy to read information and an eye catching design. We are open to either a single sided or double sided design

Colors
fbee3d
fcf5b5
fbf289
fbed22

Requirements
Must have
• The business card must include
• our logo
• our contact details as listed below:
• Dwayne Ostler
• Managing Director
• 02 6911 5033
• 0477 301 926
• wombridgehire@tallnetmail.com
Nice to have
• Nice to have a picture of machinery or part of machinery in the business card design. We would also like to incorporate our business activities which are: demolition, earthmoving, road works and cartage. It would also be highly desirable if it included a list of our machinery: Watercarts, Rollers, Excavator, Skidmule, Truck & Dog. we are open to the possibility of either single sided or double sided designs
Should not have
• should not have too many colours or detract from the main information. should not be too busy.

```html
<!DOCTYPE html>
<html lang="en">
<head>
<meta charset="utf-8">
<title>Wombridge Hire — Business Card</title>
<link rel="stylesheet" href="https://fonts.googleapis.com/css2?family=Alfa+Slab+One&family=Source+Sans+3:wght@300;400;700&display=swap">
<style>
  :root {
    --yellow: #e6ea1c;
    --black: #111111;
    --white: #ffffff;
    --paper: #f4f4f2;
    --stage: #d9d6d0;
    --grey-text: #bdbdbd;
    --grey-dark: #555555;
  }
  * { margin: 0; padding: 0; box-sizing: border-box; }
  html, body {
    width: 1200px;
    height: 902px;
    overflow: hidden;
    background: var(--stage);
    font-family: "Source Sans 3", sans-serif;
  }
  .card {
    position: absolute;
    left: 250px;
    width: 700px;
    height: 400px;
    background: var(--paper);
    overflow: hidden;
    box-shadow: 0 8px 24px rgba(0,0,0,0.22);
  }
  .card--back { top: 30px; }
  .card--front { top: 472px; }

  /* Back side */
  .back__content {
    position: absolute;
    inset: 0;
    display: flex;
    flex-direction: column;
    align-items: center;
    justify-content: center;
    gap: 14px;
  }
  .back__services {
    text-align: center;
    font-family: "Alfa Slab One", serif;
    color: var(--black);
  }
  .back__services .services__main { font-size: 46px; }
  .back__services .services__sub { margin: 8px 0 0; font-size: 28px; }
  .back__activities {
    margin-top: 14px;
    font-size: 22px;
    color: var(--grey-dark);
  }

  /* Shared pieces */
  .brand {
    display: flex;
    align-items: center;
    gap: 12px;
  }
  .brand__dot {
    width: 40px;
    height: 40px;
    border-radius: 50%;
    background: var(--yellow);
    flex: none;
  }
  .brand__name {
    font-weight: 700;
    font-size: 28px;
    color: var(--black);
    line-height: 1;
    white-space: nowrap;
  }
  .brand--large .brand__dot { width: 52px; height: 52px; }
  .brand--large .brand__name { font-size: 38px; }
  .services__main { letter-spacing: 1px; line-height: 1; white-space: nowrap; }
  .services__sub { letter-spacing: 1px; line-height: 1; white-space: nowrap; }

  /* Front side */
  .card__wave {
    position: absolute;
    inset: 0;
    width: 700px;
    height: 400px;
  }
  .front__brand {
    position: absolute;
    left: 34px;
    top: 132px;
  }
  .front__services {
    position: absolute;
    right: 28px;
    top: 34px;
    text-align: right;
    color: var(--black);
    font-family: "Alfa Slab One", serif;
  }
  .front__services .services__main { font-size: 40px; }
  .front__services .services__sub { margin-top: 8px; font-size: 25px; }
  .person {
    position: absolute;
    left: 32px;
    top: 292px;
    color: var(--white);
  }
  .person__name {
    font-weight: 300;
    font-size: 38px;
    line-height: 1;
  }
  .person__role {
    margin-top: 6px;
    font-weight: 300;
    font-size: 20px;
    color: var(--grey-text);
    line-height: 1;
  }
  .divider {
    position: absolute;
    left: 322px;
    top: 244px;
    width: 2px;
    height: 124px;
    background: var(--white);
  }
  .contacts {
    position: absolute;
    left: 342px;
    top: 250px;
    list-style: none;
    color: var(--white);
    font-weight: 300;
    font-size: 20px;
  }
  .contacts__item {
    display: flex;
    align-items: center;
    gap: 12px;
    height: 34px;
    white-space: nowrap;
  }
  .contacts__icon {
    width: 18px;
    height: 18px;
    flex: none;
  }
</style>
</head>
<body>
  <section class="card card--back" aria-label="Card back">
    <div class="back__content">
      <div class="brand brand--large">
        <span class="brand__dot"></span>
        <span class="brand__name">Wombridge Hire</span>
      </div>
      <div class="back__services">
        <div class="services__main">WATERCARTS</div>
        <div class="services__sub">ROLLERS • CARTAGE</div>
      </div>
      <p class="back__activities">Earthmoving, Demolition, Road Works &amp; Cartage</p>
    </div>
  </section>

  <section class="card card--front" aria-label="Card front">
    <svg class="card__wave" viewBox="0 0 900 514" preserveAspectRatio="none" aria-hidden="true">
      <path d="M0 300 C 250 370, 560 300, 900 195 L900 514 L0 514 Z" fill="var(--yellow)"/>
      <path d="M0 326 C 250 396, 560 326, 900 221 L900 514 L0 514 Z" fill="var(--black)"/>
    </svg>

    <div class="brand front__brand">
      <span class="brand__dot"></span>
      <span class="brand__name">Wombridge Hire</span>
    </div>

    <div class="front__services">
      <div class="services__main">WATERCARTS</div>
      <div class="services__sub">ROLLERS • CARTAGE</div>
    </div>

    <div class="person">
      <div class="person__name">Dwayne Ostler</div>
      <div class="person__role">managing director</div>
    </div>

    <div class="divider"></div>

    <ul class="contacts">
      <li class="contacts__item">
        <svg class="contacts__icon" viewBox="0 0 22 22" aria-hidden="true">
          <rect width="22" height="22" fill="#ffffff"/>
          <path d="M6 4 L9 4 L10 8 L8 9.5 C9 12 10 13 12.5 14 L14 12 L18 13 L18 16 C18 17 17 18 16 18 C9 17.5 4.5 13 4 6 C4 5 5 4 6 4 Z" fill="#111111"/>
        </svg>
        <span>02 6911 5033</span>
      </li>
      <li class="contacts__item">
        <svg class="contacts__icon" viewBox="0 0 22 22" aria-hidden="true">
          <rect width="22" height="22" fill="#ffffff"/>
          <rect x="7" y="3" width="8" height="16" rx="1.5" fill="#111111"/>
          <rect x="8.5" y="5" width="5" height="8" fill="#ffffff"/>
          <circle cx="11" cy="16" r="1" fill="#ffffff"/>
        </svg>
        <span>0477 301 926</span>
      </li>
      <li class="contacts__item">
        <svg class="contacts__icon" viewBox="0 0 22 22" aria-hidden="true">
          <rect width="22" height="22" fill="#ffffff"/>
          <rect x="3" y="6" width="16" height="11" fill="none" stroke="#111111" stroke-width="1.6"/>
          <path d="M3 6 L11 12.5 L19 6" fill="none" stroke="#111111" stroke-width="1.6"/>
        </svg>
        <span>wombridgehire@tallnetmail.com</span>
      </li>
    </ul>
  </section>
</body>
</html>
```